Website design for commercial and residential security company

we're looking to see some new designs for an established company with no website.

homepage and one inner page

here is a link to the homepage content, sitemap, logo and more.
https://files.brontavel.net/share/7QxmPzLrTw2vNkdJhYcsa9eFgbUoiVwRn?view=open

call to action should be Request A Quote

if you have any questions please send them to us asap

thank you

1 page

Sans Serif

```html
<!DOCTYPE html>
<html lang="en">
<head>
<meta charset="utf-8">
<title>Keystone Guard Solutions – Security Services</title>
<link rel="stylesheet" href="https://fonts.googleapis.com/css2?family=Montserrat:ital,wght@0,400;0,500;0,600;0,700;1,400;1,600;1,700&family=Oswald:wght@400;500&display=swap">
<style>
  :root {
    --gold: #cfad3b;
    --gold-soft: #d6b849;
    --ink: #111111;
    --grey-text: #5a5a5a;
    --grey-mid: #7a7a7a;
    --light: #f2f2f2;
    --navy: #0b1322;
    --white: #ffffff;
  }
  * { box-sizing: border-box; margin: 0; padding: 0; }
  html, body { width: 1200px; height: 4460px; overflow: hidden; }
  body { position: relative; background: var(--white); font-family: "Montserrat", sans-serif; color: var(--grey-text); }
  .abs { position: absolute; }

  /* Header */
  .site-header { position: absolute; top: 0; left: 0; width: 1200px; height: 118px; background: var(--white); }
  .brand { position: absolute; left: 78px; top: 34px; display: flex; align-items: center; gap: 10px; }
  .brand-mark { width: 14px; height: 14px; background: var(--gold); border-radius: 50%; }
  .brand-name { font-family: "Montserrat", sans-serif; font-weight: 700; font-size: 22px; color: var(--gold); line-height: 1.1; letter-spacing: 0.5px; }
  .main-nav { position: absolute; top: 44px; left: 470px; display: flex; gap: 0; font-size: 17px; color: #444; }
  .main-nav a { text-decoration: none; color: inherit; margin-right: 28px; }
  .main-nav a.active { color: var(--gold); border-bottom: 2px solid var(--gold); padding-bottom: 10px; }
  .search { position: absolute; left: 977px; top: 48px; width: 172px; height: 22px; border-bottom: 1px solid #ddd; border-left: 1px solid #ddd; font-size: 11px; color: var(--gold); padding: 6px 0 0 18px; }
  .search svg { position: absolute; right: 2px; top: 6px; }

  /* Hero */
  .hero { position: absolute; top: 118px; left: 0; width: 1200px; height: 437px; }
  .hero-photo { position: absolute; inset: 0; background: linear-gradient(180deg, #e4e4e4 0%, #d2d2d2 60%, #c6c6c6 100%); }
  .hero-camera { position: absolute; left: 778px; top: 22px; width: 422px; height: 230px; background: radial-gradient(ellipse at 40% 50%, #4a4a4e 0%, #2a2a2e 55%, rgba(200,200,200,0) 75%); }
  .hero-dots { position: absolute; left: 46px; top: 196px; display: flex; flex-direction: column; gap: 7px; }
  .hero-dots span { width: 8px; height: 8px; border-radius: 50%; background: #999; }
  .hero-dots span.on { background: var(--gold); }
  .hero-title { position: absolute; left: 148px; top: 78px; font-family: "Oswald", sans-serif; font-weight: 400; font-size: 96px; color: var(--gold); line-height: 1; }
  .hero-sub { position: absolute; left: 153px; top: 192px; font-size: 34px; font-weight: 500; letter-spacing: 19px; color: #555; }
  .btn { display: inline-block; font-weight: 600; font-size: 18px; color: var(--white); text-align: center; border-radius: 2px; }
  .btn-gold { background: var(--gold); }
  .btn-grey { background: #7d7d7d; }
  .hero .btn { position: absolute; top: 342px; height: 50px; line-height: 50px; }

  /* Mission */
  .section-title { font-weight: 500; font-size: 54px; line-height: 1.1; color: #6a6a6a; }
  .section-title em { font-style: normal; color: var(--gold); }
  .lead { font-style: italic; font-size: 18px; line-height: 26px; color: var(--gold); }
  .body-copy { font-size: 14.5px; line-height: 27px; color: var(--grey-text); }
  .frame-gold { position: absolute; background: var(--gold); }
  .photo { position: absolute; }

  /* Commercial */
  .band { position: absolute; left: 0; width: 1200px; background: var(--gold); }
  .band-title { position: absolute; left: 0; width: 1200px; text-align: center; font-weight: 500; font-size: 64px; color: var(--white); letter-spacing: 2px; }
  .band-text { position: absolute; left: 90px; width: 1020px; text-align: center; font-size: 20px; line-height: 34px; color: var(--ink); font-weight: 500; }
  .method-title { position: absolute; left: 0; width: 1200px; text-align: center; font-size: 56px; color: var(--ink); font-weight: 500; letter-spacing: 2px; }
  .method-card { position: absolute; left: 84px; top: 1438px; width: 840px; height: 537px; background: var(--white); border: 1px solid #e6d9a8; }
  .method-panel { position: absolute; left: 102px; top: 1468px; width: 518px; height: 487px; background: #fafafa; box-shadow: 0 0 6px rgba(0,0,0,0.06); padding: 28px 18px 0 18px; }
  .method-panel h3 { font-weight: 500; font-size: 20px; line-height: 25px; color: var(--gold); padding-left: 0; margin-bottom: 26px; }
  .checks { list-style: none; }
  .checks li { position: relative; padding-left: 39px; font-size: 15px; line-height: 19px; color: #555; margin-bottom: 26px; }
  .checks li svg { position: absolute; left: 0; top: 0; }
  .quote { position: absolute; left: 90px; width: 1020px; text-align: center; font-style: italic; font-weight: 700; font-size: 24px; line-height: 40px; color: #6d6d6d; letter-spacing: 0.5px; }
  .band-copy { position: absolute; left: 80px; width: 1040px; text-align: center; font-size: 22px; line-height: 37px; color: var(--white); letter-spacing: 0.6px; }
  .band-copy p { margin-bottom: 5px; }

  /* Contact */
  .contact { position: absolute; left: 0; top: 3235px; width: 1200px; height: 890px; background: var(--light); }
  .contact h2 { position: absolute; left: 0; top: 75px; width: 1200px; text-align: center; font-weight: 500; font-size: 56px; color: var(--gold); letter-spacing: 1px; }
  .field { position: absolute; width: 482px; height: 68px; border: 1px solid #9a9a9a; background: var(--light); font-size: 18px; color: #777; padding: 22px 16px; }
  .field-wide { width: 1033px; height: 178px; }
  .submit { position: absolute; left: 506px; top: 768px; width: 186px; height: 63px; line-height: 63px; font-size: 22px; }

  /* Footer */
  .site-footer { position: absolute; left: 0; top: 4125px; width: 1200px; height: 335px; background: var(--navy); }
  .site-footer .brand { left: 84px; top: 32px; }
  .site-footer .brand-name { font-size: 30px; }
  .footer-text { position: absolute; left: 84px; top: 92px; width: 370px; font-size: 14.5px; line-height: 22px; color: var(--gold); }
  .footer-heading { position: absolute; left: 888px; top: 30px; font-weight: 600; font-size: 24px; color: var(--gold); border-bottom: 2px solid var(--gold); padding-bottom: 6px; }
  .footer-rule { position: absolute; left: 84px; top: 265px; width: 1034px; height: 1px; background: #3a4456; }
</style>
</head>
<body>

<header class="site-header">
  <div class="brand"><span class="brand-mark"></span><span class="brand-name">KEYSTONE GUARD</span></div>
  <nav class="main-nav">
    <a class="active" href="#">Home</a>
    <a href="#">About</a>
    <a href="#">Solutions</a>
    <a href="#">Resources</a>
    <a href="#">Contact</a>
  </nav>
  <div class="search">Search
    <svg width="10" height="10" viewBox="0 0 10 10"><circle cx="4" cy="4" r="3" fill="none" stroke="#bbb" stroke-width="1.2"/><line x1="6.3" y1="6.3" x2="9" y2="9" stroke="#bbb" stroke-width="1.2"/></svg>
  </div>
</header>

<section class="hero">
  <div class="hero-photo" role="img" aria-label="Faded black and white photo of office towers"></div>
  <div class="hero-camera" role="img" aria-label="Photo of a dark wall-mounted security camera"></div>
  <div class="hero-dots"><span class="on"></span><span></span><span></span></div>
  <h1 class="hero-title">Call to Action</h1>
  <div class="hero-sub">Security Services</div>
  <a class="btn btn-gold" style="left:155px;width:152px;">Get Quotes</a>
  <a class="btn btn-grey" style="left:333px;width:151px;">Learn more</a>
</section>

<section class="mission">
  <h2 class="section-title abs" style="left:84px;top:620px;">Our <em>Mission</em></h2>
  <p class="lead abs" style="left:84px;top:696px;width:470px;">To provide our customers with&nbsp; comprehensive security, audio/video, and automation with top notch customer service. We Ensure Security with Smart Tools.</p>
  <p class="body-copy abs" style="left:84px;top:814px;width:490px;">The graded security measures from Keystone Guard Solutions ensure the safety of both residential and commercial property. We provide a wide range of Residential and Commercial Security Solutions.</p>
  <a class="btn btn-gold abs" style="left:84px;top:948px;width:152px;height:50px;line-height:50px;">Read More</a>
  <div class="frame-gold" style="left:652px;top:603px;width:466px;height:332px;"></div>
  <div class="photo" role="img" aria-label="Grey photo of a security camera hanging from a pole against a cloudy sky" style="left:623px;top:630px;width:469px;height:338px;background:linear-gradient(160deg,#8a8a8a 0%,#cfcfcf 45%,#a9a9a9 100%);"></div>
</section>

<section class="commercial">
  <div class="band" style="top:1062px;height:678px;"></div>
  <svg class="abs" style="left:584px;top:1088px;" width="32" height="50" viewBox="0 0 32 50">
    <circle cx="16" cy="18" r="13" fill="#111"/>
    <rect x="10" y="33" width="12" height="4" fill="#111"/>
    <rect x="11" y="39" width="10" height="4" fill="#111"/>
    <path d="M18 8 L11 20 H16 L14 28 L21 16 H16 Z" fill="#cfad3b"/>
  </svg>
  <h2 class="band-title" style="top:1148px;">Commercial Solutions</h2>
  <p class="band-text" style="top:1236px;">People's safety is our top priority. This includes ensuring that the security system built at your commercial property is configured accurately. Further, it will protect against intruders, burglaries, and holdups.</p>
  <h2 class="method-title" style="top:1358px;">We Do This By</h2>
  <div class="method-card"></div>
  <div class="method-panel">
    <h3>Protect assets and Security of your business with Exceptional Commercial Security Installation</h3>
    <ul class="checks">
      <li><svg width="22" height="22" viewBox="0 0 22 22"><rect x="1" y="4" width="17" height="17" fill="none" stroke="#222" stroke-width="2"/><path d="M5 11 L9 16 L20 2" fill="none" stroke="#222" stroke-width="2.4"/></svg>Audio &amp; Video Solutions for your commercial property</li>
      <li><svg width="22" height="22" viewBox="0 0 22 22"><rect x="1" y="4" width="17" height="17" fill="none" stroke="#222" stroke-width="2"/><path d="M5 11 L9 16 L20 2" fill="none" stroke="#222" stroke-width="2.4"/></svg>Burglar Alarms &amp; Detectors</li>
      <li><svg width="22" height="22" viewBox="0 0 22 22"><rect x="1" y="4" width="17" height="17" fill="none" stroke="#222" stroke-width="2"/><path d="M5 11 L9 16 L20 2" fill="none" stroke="#222" stroke-width="2.4"/></svg>CCTV cameras equipped with facial recognition technologies enable the technology to identify the offenders.</li>
      <li><svg width="22" height="22" viewBox="0 0 22 22"><rect x="1" y="4" width="17" height="17" fill="none" stroke="#222" stroke-width="2"/><path d="M5 11 L9 16 L20 2" fill="none" stroke="#222" stroke-width="2.4"/></svg>Monitoring of alarms and video recordings 24 hours a day, seven days a week. Addressing all the incidents with an urgent response.</li>
      <li><svg width="22" height="22" viewBox="0 0 22 22"><rect x="1" y="4" width="17" height="17" fill="none" stroke="#222" stroke-width="2"/><path d="M5 11 L9 16 L20 2" fill="none" stroke="#222" stroke-width="2.4"/></svg>Alarm systems and cameras precisely installed so that more of your property is tracked.</li>
    </ul>
  </div>
  <div class="photo" role="img" aria-label="Close-up photo of a safe combination dial" style="left:650px;top:1468px;width:550px;height:477px;background:radial-gradient(circle at 48% 50%,#6a6a6a 0%,#2e2e2e 35%,#cfcfcf 62%,#e2e2e2 100%);"></div>
  <p class="quote" style="top:2014px;">We will help secure your company outside of the realm of conventional monitoring technologies. Indeed, we take a customised and comprehensive approach to defence.</p>
  <div class="band" style="top:2170px;height:420px;"></div>
  <div class="band-copy" style="top:2188px;">
    <p>Flooding, smoke, power outages, temperature fluctuations, and other factors will all be tracked. So, you can take prompt steps before you experience damage.</p>
    <p>But, it all comes down to internal and external security measures.</p>
    <p>We can combine low-light cameras, smoke and temperature monitoring, noise control, and physical surveillance into a 24/7 commercial security solution. Thus, you can focus on running your business with utmost safety.</p>
    <p>Our commercial security services are comprehensive. In fact, we have worked out how to protect companies from future threats by tailoring our strategy to each new customer. Therefore, whatever business you are into, we provide you with a security solution that physically protects you, your employees, clients, and property.</p>
  </div>
</section>

<section class="residential">
  <h2 class="section-title abs" style="left:84px;top:2664px;">Residential<br><em>Security Solutions</em></h2>
  <p class="lead abs" style="left:84px;top:2816px;width:490px;">Consider a home surveillance device that would do more for you and your family than you ever imagined.</p>
  <p class="body-copy abs" style="left:84px;top:2902px;width:490px;">Keystone Guard Solutions is your trustable security provider. Also, as certified professionals carry out the installation, you have everything under control. Your home is being securely watched from various points, with cameras capable of tracking any intruder's path. Specifically, we offer Residential Intrusion Detection Security Systems, Residential Alarm, Residential Network Wi-Fi, CCTVs and residential home automation.</p>
  <a class="btn btn-gold abs" style="left:84px;top:3142px;width:152px;height:50px;line-height:50px;">Read More</a>
  <div class="frame-gold" style="left:663px;top:2705px;width:455px;height:370px;"></div>
  <div class="photo" role="img" aria-label="Photo of a security camera mounted under the eaves of a house" style="left:623px;top:2730px;width:471px;height:412px;background:linear-gradient(135deg,#5a4636 0%,#3a3632 45%,#b9b6b0 100%);"></div>
</section>

<section class="contact">
  <h2>Get in touch with us today!</h2>
  <div class="field" style="left:85px;top:210px;">Full Name</div>
  <div class="field" style="left:636px;top:210px;">Company</div>
  <div class="field" style="left:85px;top:315px;">Email</div>
  <div class="field" style="left:636px;top:315px;">Phone</div>
  <div class="field" style="left:85px;top:421px;">Services Location ( Address )</div>
  <div class="field" style="left:636px;top:421px;">Services Location ( City,State,Zip Code )</div>
  <div class="field field-wide" style="left:85px;top:527px;">Description of Services (s) Needed, Which Day \ Date ete..</div>
  <a class="btn btn-gold submit">Submit</a>
</section>

<footer class="site-footer">
  <div class="brand"><span class="brand-mark"></span><span class="brand-name">KEYSTONE GUARD</span></div>
  <p class="footer-text">To provide our customers with&nbsp; comprehensive security, audio/video, and automation with top notch customer service. We Ensure Security with Smart Tools.</p>
  <div class="footer-heading">Contact Info</div>
  <div class="footer-rule"></div>
</footer>

</body>
</html>
```